We Buy Houses Postcard Design

Harborline Estate Partners is one of Baltimore‘s top real estate investing groups because we treat buyers and sellers like real people; not like numbers on a spreadsheet. We specialize in buying distressed properties including multi-family, commercial, retail, single family, and bank REO’s from sellers who need to sell fast. Our website is www.fernwickhomebuyers.example. Our phone number is (443) 517-2940. Both need to be on the card. Front and back sides are to be printed. Front full color, back black and white. We want our logo on the design somewhere. The logo can be found on the website. If you need the original files ask me for them. See attached as examples. Return address should be 487 W Garnet Ave, Suite 318, Baltimore, MD 21201. My name is Gregory. Address label is 1" x 2-5/8". Please leave room for it and postage on the back side.

Industry/Entity Type

Real Estate

```html
<!DOCTYPE html>
<html lang="en">
<head>
<meta charset="utf-8">
<title>We Buy Houses – Harborline Estate Partners</title>
<link rel="stylesheet" href="https://fonts.googleapis.com/css2?family=Arimo:wght@700&display=swap">
<style>
  :root {
    --stage-light: #e9eaeb;
    --stage-dark: #c4c6c8;
    --card-blue: #0b69ab;
    --panel-navy: #1f4c78;
    --label-blue: #1d5889;
    --white: #ffffff;
    --sky-light: #dcebfb;
    --sky-mid: #8fbdea;
    --sky-deep: #3f86d2;
  }
  * { margin: 0; padding: 0; box-sizing: border-box; }
  html, body { width: 1200px; height: 1000px; overflow: hidden; }
  body {
    background: radial-gradient(ellipse at center, var(--stage-light) 0%, var(--stage-dark) 100%);
    position: relative;
    font-family: "Arimo", Arial, sans-serif;
  }
  .postcard {
    position: absolute;
    left: 101px; top: 142px;
    width: 998px; height: 716px;
    background: var(--card-blue);
    box-shadow: 0 0 3px rgba(0,0,0,0.15);
    overflow: hidden;
  }
  .headline {
    position: absolute;
    left: 0; width: 100%;
    text-align: center;
    font-family: "Arimo", Arial, sans-serif;
    font-weight: 700;
    line-height: 1;
    white-space: nowrap;
    background: linear-gradient(160deg, var(--sky-light) 0%, var(--sky-mid) 35%, var(--sky-deep) 60%, var(--sky-mid) 80%, var(--sky-light) 100%);
    -webkit-background-clip: text;
    background-clip: text;
    color: transparent;
    -webkit-text-stroke: 2px var(--white);
  }
  .headline-top { top: 53px; font-size: 230px; letter-spacing: -4px; }
  .headline-bottom { top: 255px; font-size: 200px; letter-spacing: -5px; }
  .benefits { position: absolute; left: 0; top: 470px; width: 998px; height: 63px; }
  .benefit {
    position: absolute; top: 0; height: 63px;
    background: var(--white);
    color: var(--label-blue);
    font-size: 45px; font-weight: 700;
    display: flex; align-items: center; justify-content: center;
    letter-spacing: 0.5px;
  }
  .benefit-condition { left: 0; width: 514px; border-bottom-right-radius: 30px; }
  .benefit-closing { left: 529px; width: 469px; border-top-left-radius: 30px; }
  .contact-panel {
    position: absolute; left: 0; top: 553px;
    width: 641px; height: 137px;
    background: var(--panel-navy);
    color: var(--white);
  }
  .contact-phone {
    position: absolute; left: 100px; top: 8px;
    font-size: 82px; font-weight: 700; letter-spacing: -0.5px;
    line-height: 1.1;
  }
  .contact-web {
    position: absolute; left: 100px; top: 94px;
    font-size: 25px; font-weight: 700;
  }
  .brand-box {
    position: absolute; left: 659px; top: 553px;
    width: 339px; height: 137px;
    background: var(--white);
    display: flex; align-items: center; justify-content: center; gap: 12px;
    padding: 0 18px;
  }
  .brand-dot { width: 18px; height: 18px; border-radius: 50%; background: var(--card-blue); flex: none; }
  .brand-name {
    color: var(--label-blue);
    font-size: 27px; font-weight: 700; line-height: 1.15;
    text-align: center;
  }
</style>
</head>
<body>
  <main class="postcard">
    <h1 class="headline headline-top">WE BUY</h1>
    <div class="headline headline-bottom">HOUSES</div>
    <div class="benefits">
      <div class="benefit benefit-condition">ANY CONDITION</div>
      <div class="benefit benefit-closing">FAST CLOSING</div>
    </div>
    <section class="contact-panel">
      <div class="contact-phone">443-517-2940</div>
      <div class="contact-web">www.fernwickhomebuyers.example</div>
    </section>
    <div class="brand-box">
      <span class="brand-dot"></span>
      <span class="brand-name">Harborline Estate Partners</span>
    </div>
  </main>
</body>
</html>
```